Design an Elegant Handbag Brand website

I need a webiste design are looking for ideas for a new theme, color scheme, etc. You come up with the general look and feel of the home page and our team will take it from there.
We're only looking for a one (1) page layout which should be fashionable and graphic intensive, but also include the standard homepage links (about us, see our collections, etc)

Target Market(s)

Our customers are fashionable women looking for an animal friendly and environmentally friendly handbag.

Industry/Entity Type

Business

Number of Pages Required

1 page

Font styles to use
Serif
Sans Serif

Requirements
Must have
• Feel free to modify it with different colors or tweaks as you see fit. We are open to all suggestions.
Nice to have

```html
<!DOCTYPE html>
<html lang="en">
<head>
<meta charset="utf-8">
<title>Company Name – Handbags</title>
<link href="https://fonts.googleapis.com/css2?family=Montserrat:ital,wght@0,300;0,400;0,500;0,700;1,400&family=Great+Vibes&display=swap" rel="stylesheet">
<style>
:root{
  --gold:#a4916b;
  --gold-dark:#8f7c57;
  --ink:#1c1c1c;
  --text:#555;
  --muted:#777;
  --line:#cfcfcf;
  --white:#fff;
  --black:#000;
  --field:#efefef;
}
*{box-sizing:border-box;margin:0;padding:0}
html,body{width:1200px;height:4906px;overflow:hidden;background:var(--white)}
body{position:relative;font-family:"Montserrat",sans-serif;color:var(--ink)}
.abs{position:absolute}
.script{font-family:"Great Vibes",cursive;font-weight:400}
.photo{position:absolute}

/* header */
.brand{left:51px;top:22px;font-size:34px;font-weight:400;letter-spacing:1px;color:#222}
.nav{right:52px;top:38px;display:flex;gap:32px;font-size:17px;color:#222}

/* hero */
.hero-photo{left:0;top:0;width:1200px;height:619px;background:linear-gradient(90deg,#e9e2dc 0%,#d8cfc7 30%,#ece6e1 60%,#f3efec 100%)}
.hero-copy{left:700px;width:452px;top:175px;text-align:center}
.hero-copy .script{font-size:64px;color:#222;line-height:1}
.hero-copy .lead{font-size:42px;font-weight:300;letter-spacing:1px;margin-top:14px;line-height:1.1}
.hero-copy h1{font-size:42px;font-weight:700;line-height:1.2}
.hero-copy p{font-size:21px;color:#333;line-height:28px;margin-top:20px}
.btn-solid{display:inline-block;margin-top:30px;padding:11px 48px;background:var(--gold);color:var(--white);font-weight:700;font-size:19px;outline:2px solid #d9cfbb;outline-offset:-5px}

/* feature tiles */
.tile{position:absolute;background:var(--gold);color:var(--white)}
.tile .script{font-size:46px;line-height:1}
.tile h3{font-size:21px;font-weight:700;line-height:29px;margin-top:6px}
.tile p{font-size:15px;line-height:24px;margin-top:8px;color:#f3ede2}
.btn-line{display:inline-block;margin-top:24px;padding:12px 14px;border:2px solid var(--white);font-weight:700;font-size:16px;color:var(--white)}

/* section titles */
.section-title{left:0;width:1200px;text-align:center;font-size:52px;font-weight:400;color:#111}

/* collections */
.card{position:absolute;width:259px;height:267px;border:6px solid #f2f2f2;box-shadow:0 0 2px #ddd}
.product{position:absolute;width:259px;text-align:center}
.product h4{font-size:24px;font-weight:700;color:#111}
.product span{display:block;font-size:16px;color:var(--text);margin-top:4px}
.product svg{margin-top:12px}

/* about */
.about-panel{left:51px;top:2469px;width:446px;height:606px;background:var(--black);color:var(--white);padding:76px 30px 0 30px}
.about-panel h2{font-size:50px;font-weight:400;line-height:52px}
.about-panel h2 em{font-style:normal;color:var(--gold)}
.about-panel .script{color:var(--gold);font-size:54px;margin-top:20px;line-height:1}
.about-panel p{font-size:18px;line-height:29px;margin-top:14px}
.quote-panel{left:598px;top:3075px;width:551px;height:424px;background:var(--gold);color:var(--white);text-align:center}
.avatar{position:absolute;left:217px;top:46px;width:114px;height:114px;border-radius:50%;background:radial-gradient(circle,#e4c3b4,#8e6b5d);border:3px solid #b8a683}
.quote-panel blockquote{position:absolute;left:40px;right:40px;top:180px;font-style:italic;font-size:20px;line-height:28px;color:#f5efe4}
.quote-panel .author{position:absolute;left:0;right:0;top:308px;font-size:19px;line-height:24px}
.quote-panel .author b{display:block}

/* news */
.post-date{position:absolute;font-size:16px;letter-spacing:4px;color:#333;transform:rotate(-90deg);transform-origin:left top;white-space:nowrap}
.post{position:absolute;width:316px}
.post h5{font-size:20px;font-weight:400;color:var(--gold-dark);line-height:26px}
.post p{font-size:15px;line-height:25px;color:var(--text);margin-top:12px}

/* newsletter */
.subscribe{left:238px;top:4383px;width:724px;height:56px;background:var(--field);border:1px solid #ddd;display:flex;align-items:center;justify-content:space-between;padding:0 28px 0 18px;font-size:16px;color:#666}

/* footer */
.rule{left:51px;width:1098px;height:2px;background:var(--line)}
.footer-col{position:absolute;top:4528px}
.footer-col h6{font-size:25px;font-weight:700;color:#222}
.footer-col ul{list-style:none;margin-top:20px}
.footer-col li{font-size:16px;line-height:32.5px;color:#333}
.contact li{display:flex;gap:14px;align-items:flex-start;line-height:24px;margin-bottom:18px}
.contact svg{flex:none;margin-top:2px}
.copyright{left:51px;top:4852px;font-size:14px;color:#333}
.social{right:51px;top:4837px;display:flex;gap:8px}
.social span{width:38px;height:38px;border-radius:50%;border:2px solid var(--gold)}
</style>
</head>
<body>

<!-- header & hero -->
<div class="photo hero-photo" role="img" aria-label="Woman in a wide-brim hat holding a dark leather tote bag, soft light interior"></div>
<div class="abs brand">Company Name</div>
<nav class="abs nav"><span>Collection</span><span>About</span><span>News</span><span>Contact Us</span></nav>
<div class="abs hero-copy">
  <div class="script">Phasellus Magna</div>
  <div class="lead">THE LARGEST</div>
  <h1>Range Of handbags</h1>
  <p>hasellus magna tellus, imperdietsed<br>fermentum in, lobortis id sem.</p>
  <span class="btn-solid">View Collection</span>
</div>

<!-- feature row one -->
<div class="photo" style="left:51px;top:587px;width:818px;height:444px;background:linear-gradient(120deg,#6d5a4a 0%,#8b8177 35%,#5a7298 60%,#a09a92 100%)" role="img" aria-label="Woman in jeans and heels seated on stone steps beside a brown leather handbag"></div>
<div class="tile" style="left:869px;top:620px;width:280px;height:411px;padding:52px 20px 0 20px">
  <div class="script">Nulla facilisi</div>
  <h3>Curabitur elemem<br>lorem eget bibeum<br>molli</h3>
  <p>Aliquam ac justo blandit nibh scelerisque eleifend. Praesent posuere quam</p>
  <span class="btn-line">View Collection</span>
</div>

<!-- feature row two -->
<div class="tile" style="left:51px;top:1031px;width:383px;height:367px;padding:50px 45px 0 45px">
  <div class="script">Nulla facilisi</div>
  <h3>Curabitur elemem lorem<br>eget bibeum molli</h3>
  <p>Aliquam ac justo blandit nibh sceler isque eleifend. Praesent posuere quam</p>
  <span class="btn-line">View Collection</span>
</div>
<div class="photo" style="left:434px;top:1031px;width:381px;height:367px;background:radial-gradient(ellipse at 50% 55%,#b59f80 0%,#d4c6b2 45%,#fff 75%)" role="img" aria-label="Set of three beige handbags with tassel charm"></div>
<div class="photo" style="left:815px;top:1031px;width:385px;height:367px;background:linear-gradient(90deg,#5f6166 0%,#7a7c80 40%,#3b3a3c 70%,#8a8b8f 100%)" role="img" aria-label="Smiling woman in leather jacket with grey handbag against a metal wall"></div>

<!-- collections -->
<h2 class="abs section-title" style="top:1474px">Our Collections</h2>

<div class="card" role="img" aria-label="Black leather tote bag" style="left:51px;top:1564px;background:radial-gradient(ellipse at 50% 55%,#222 0%,#444 30%,#fff 55%)"></div>
<div class="card" role="img" aria-label="Peach dome handbag with strap" style="left:331px;top:1564px;background:radial-gradient(ellipse at 50% 55%,#f1c59c 0%,#f3d3b6 32%,#fff 58%)"></div>
<div class="card" role="img" aria-label="Bright blue handbag" style="left:610px;top:1564px;background:radial-gradient(ellipse at 50% 55%,#1e73c9 0%,#3a8ad8 30%,#fff 56%)"></div>
<div class="card" role="img" aria-label="Dusty pink handbag" style="left:890px;top:1564px;background:radial-gradient(ellipse at 50% 55%,#c9998a 0%,#d8b3a7 32%,#fff 58%)"></div>

<div class="product" style="left:51px;top:1858px"><h4>Sendisse Fermum</h4><span>Turpis ut Dignissim</span><svg width="22" height="14" viewBox="0 0 22 14"><path d="M1 7h19M14 1l6 6-6 6" fill="none" stroke="#555" stroke-width="2"/></svg></div>
<div class="product" style="left:331px;top:1858px"><h4>Sendisse Fermum</h4><span>Turpis ut Dignissim</span><svg width="22" height="14" viewBox="0 0 22 14"><path d="M1 7h19M14 1l6 6-6 6" fill="none" stroke="#555" stroke-width="2"/></svg></div>
<div class="product" style="left:610px;top:1858px"><h4>Sendisse Fermum</h4><span>Turpis ut Dignissim</span><svg width="22" height="14" viewBox="0 0 22 14"><path d="M1 7h19M14 1l6 6-6 6" fill="none" stroke="#555" stroke-width="2"/></svg></div>
<div class="product" style="left:890px;top:1858px"><h4>Sendisse Fermum</h4><span>Turpis ut Dignissim</span><svg width="22" height="14" viewBox="0 0 22 14"><path d="M1 7h19M14 1l6 6-6 6" fill="none" stroke="#555" stroke-width="2"/></svg></div>

<div class="card" role="img" aria-label="Glossy white handbag" style="left:51px;top:1993px;background:radial-gradient(ellipse at 50% 55%,#e4e3da 0%,#eeeee8 34%,#fff 60%)"></div>
<div class="card" role="img" aria-label="Navy slouch handbag" style="left:331px;top:1993px;background:radial-gradient(ellipse at 50% 55%,#2b3858 0%,#445274 32%,#fff 58%)"></div>
<div class="card" role="img" aria-label="Royal blue tote bag" style="left:610px;top:1993px;background:radial-gradient(ellipse at 50% 58%,#2a4fa6 0%,#4065b8 32%,#fff 58%)"></div>
<div class="card" role="img" aria-label="Salmon pink handbag with charm" style="left:890px;top:1993px;background:radial-gradient(ellipse at 50% 55%,#eeaa95 0%,#f2c2b2 32%,#fff 58%)"></div>

<div class="product" style="left:51px;top:2286px"><h4>Sendisse Fermum</h4><span>Turpis ut Dignissim</span><svg width="22" height="14" viewBox="0 0 22 14"><path d="M1 7h19M14 1l6 6-6 6" fill="none" stroke="#555" stroke-width="2"/></svg></div>
<div class="product" style="left:331px;top:2286px"><h4>Sendisse Fermum</h4><span>Turpis ut Dignissim</span><svg width="22" height="14" viewBox="0 0 22 14"><path d="M1 7h19M14 1l6 6-6 6" fill="none" stroke="#555" stroke-width="2"/></svg></div>
<div class="product" style="left:610px;top:2286px"><h4>Sendisse Fermum</h4><span>Turpis ut Dignissim</span><svg width="22" height="14" viewBox="0 0 22 14"><path d="M1 7h19M14 1l6 6-6 6" fill="none" stroke="#555" stroke-width="2"/></svg></div>
<div class="product" style="left:890px;top:2286px"><h4>Sendisse Fermum</h4><span>Turpis ut Dignissim</span><svg width="22" height="14" viewBox="0 0 22 14"><path d="M1 7h19M14 1l6 6-6 6" fill="none" stroke="#555" stroke-width="2"/></svg></div>

<!-- about -->
<div class="abs about-panel">
  <h2>About<br><em>Our Handbags</em></h2>
  <div class="script">Mauris Pellentesque</div>
  <p>Nec mauris id vulputate. Morbi ultrices, enim in fermentum ultricies, magna lorem elementum dolor, quis ornare dolor sapien sit amet lacus. Donec lacinia rutrum felis, non fermentum dui ultricies in. Sed nec eleifend felis. Aenean sagittis tortor in turpis lobortis porta. Praesent porttitor elit mauris, eget consequat ante scelerisque nec.</p>
</div>
<div class="photo" style="left:497px;top:2469px;width:652px;height:606px;background:linear-gradient(135deg,#7d7770 0%,#a08c6e 35%,#c8902f 55%,#3d3a37 80%,#6b6661 100%)" role="img" aria-label="Woman in mustard sweater and striped trousers crouching on a city street with a tan tote bag"></div>

<div class="photo" style="left:51px;top:3075px;width:547px;height:424px;background:radial-gradient(ellipse at 55% 65%,#b3202a 0%,#5a1a1c 30%,#1b1a1d 65%,#0e0e10 100%)" role="img" aria-label="Red handbag resting on a faux fur throw in a dim candlelit room"></div>
<div class="abs quote-panel">
  <div class="avatar" role="img" aria-label="Customer portrait"></div>
  <blockquote>Cras ac consectetur nibh. Nunc eu sapien rhoncus, feugiat ex a, varius ante. Nam id dictum neque. Praesent suscipit nisl at purus mattis volutpat.</blockquote>
  <div class="author"><b>Duis auctor</b>consequat turpis</div>
</div>

<!-- news -->
<h2 class="abs section-title" style="top:3577px">Our News</h2>

<div class="post-date" style="left:50px;top:3825px">09/11/2019</div>
<div class="photo" style="left:90px;top:3659px;width:314px;height:360px;background:linear-gradient(160deg,#c9bfb8 0%,#efe9e6 40%,#2a2a2a 70%,#b8473f 100%)" role="img" aria-label="Smiling woman in white shirt carrying a black handbag"></div>
<div class="post" style="left:90px;top:4040px">
  <h5>Nam id dictum neque.<br>Praesent suscipit nisl at purus</h5>
  <p>mattis volutpat. Etiam iaculis quam et gravida interdum. Duis auctor consequat turpis. Nulla imperdiet nisl quis lacinia lacinia. Cras nec luctus elit.</p>
</div>

<div class="post-date" style="left:421px;top:3890px">09/11/2019</div>
<div class="photo" style="left:459px;top:3724px;width:316px;height:360px;background:linear-gradient(160deg,#f2e15a 0%,#f6ec9c 40%,#a7733f 65%,#f1dd58 100%)" role="img" aria-label="Woman in yellow floral dress holding a tan saddle bag"></div>
<div class="post" style="left:459px;top:4105px">
  <h5>Nam id dictum neque.<br>Praesent suscipit nisl at purus</h5>
  <p>mattis volutpat. Etiam iaculis quam et gravida interdum. Duis auctor consequat turpis. Nulla imperdiet nisl quis lacinia lacinia. Cras nec luctus elit.</p>
</div>

<div class="post-date" style="left:792px;top:3825px">09/11/2019</div>
<div class="photo" style="left:831px;top:3659px;width:316px;height:360px;background:linear-gradient(170deg,#d8dde2 0%,#c9c4bb 35%,#b1172b 60%,#1d1f24 100%)" role="img" aria-label="Woman in red dress and straw hat carrying a black handbag on a city street"></div>
<div class="post" style="left:831px;top:4040px">
  <h5>Nam id dictum neque.<br>Praesent suscipit nisl at purus</h5>
  <p>mattis volutpat. Etiam iaculis quam et gravida interdum. Duis auctor consequat turpis. Nulla imperdiet nisl quis lacinia lacinia. Cras nec luctus elit.</p>
</div>

<!-- newsletter -->
<div class="abs subscribe">
  <span>Enter your mail id</span>
  <svg width="24" height="22" viewBox="0 0 24 22"><path d="M1 11 23 1 17 21 11 13Z M11 13 23 1" fill="var(--gold)" stroke="var(--gold)" stroke-linejoin="round"/></svg>
</div>

<div class="abs rule" style="top:4476px"></div>

<!-- footer -->
<div class="footer-col contact" style="left:51px">
  <h6>Contact us</h6>
  <ul>
    <li><svg width="16" height="20" viewBox="0 0 16 20"><path d="M8 1a6.5 6.5 0 0 0-6.5 6.5C1.5 12 8 19 8 19s6.5-7 6.5-11.5A6.5 6.5 0 0 0 8 1Z" fill="#222"/><circle cx="8" cy="7.5" r="2.4" fill="#fff"/></svg><span>870 Harbor Point Avenue FL<br>33401 USA</span></li>
    <li><svg width="16" height="20" viewBox="0 0 16 20"><path d="M5 1h-2.5a1.5 1.5 0 0 0-1.5 1.6c.3 7.8 5 13.7 11.8 15.4l2-3.2-3.3-2-1.6 1.8C7 13.4 5.6 10.8 5 8l2.3-1.2Z" fill="#222"/></svg><span>+100 555 010 20</span></li>
    <li><svg width="18" height="14" viewBox="0 0 18 14"><rect x="1" y="1" width="16" height="12" fill="#222"/><path d="M1 1l8 6.5L17 1" fill="none" stroke="#fff" stroke-width="1.4"/></svg><span>hello@marelleshop.com</span></li>
  </ul>
</div>
<div class="footer-col" style="left:362px">
  <h6>Home</h6>
  <ul><li>Maecenas vulputate</li><li>Enim id cursus.</li><li>Phasellus magna</li><li>Imperdiet</li><li>Fermentum</li><li>Lobortis</li></ul>
</div>
<div class="footer-col" style="left:632px">
  <h6>About</h6>
  <ul><li>Maecenas vulputate</li><li>Enim id cursus.</li><li>Phasellus magna</li><li>Imperdiet</li><li>Fermentum</li><li>Lobortis</li></ul>
</div>
<div class="footer-col" style="left:895px">
  <h6>Bag</h6>
  <ul><li>Maecenas vulputate</li><li>Enim id cursus.</li><li>Phasellus magna</li><li>Imperdiet</li><li>Fermentum</li><li>Lobortis</li></ul>
</div>

<div class="abs rule" style="top:4822px"></div>
<div class="abs copyright">© 2020 - Your Company Name. All Right Reserved.</div>
<div class="abs social" aria-label="Social links"><span></span><span></span><span></span><span></span></div>

</body>
</html>
```